依頼詳細
某ホテルのブライダルフェアや内覧会(結婚が決まったカップルが衣装や引き出物などを選ぶイベント)などでお客様に配布します。お客様にこのチラシを見せながら内容を説明したりもするので、わかりやすい料金とコース内容が伝えられるデザインをお願いします。
記載項目
屋号/電話番号/料金プラン/なにか良いキャッチフレーズなどあればお願いしたいです。
サイズ
A4
ページ数
片面
希望イメージ
シンプル 複雑
単色 カラフル
暗い 明るい
日常 高級
遊び心 厳粛
未来的 伝統的
女性的 男性的
希望する色
オレンジ、緑など「新鮮」「明るい」イメージ色を希望します。
納品ファイル
• イラストレーター形式 (.ai)
• フォトショップ形式 (.psd)
補足説明
いままでは市販のワープロソフトなどで付属のテンプレートなどを元に作ってきましたが、
やはりプロの広告を出している他社と大きく差がついてしまっています。 もう自分でデザインしていては他社と差が広がるばかりと感じ、今回依頼させていただきます。よろしくお願いいたします。
当方の使用していたチラシです
遅れてすみませんでした。映っている本人たちに許可は取りました。よろしくお願いいたします。
■ 選んだ理由

最終的にお二方の提案を残させていただきましたが、通り過ぎるようとするお客様の目を止まらせ、それでいて優先される物が目立ち、シンプルにまとまっていてちょっとポップな感じで同ビデオ業者との差別化をはかっているこの提案を選ばせていただきました。

■ 提案者全員のお礼・コメント

この度は当方の依頼に対して、予想以上に多くのクリエーターの方々から、想像以上にハイクオリティーな提案を多数いただき心から感謝しております。
本当にどれを選んで良い物かかなり悩みました。改めてこのサイトの素晴らしさを実感いたしました。次回また商品内容を変える際には間違いなくここに依頼させていただきます。
提案を下さったすべてのクリエーターの皆様に感謝申し上げます。
ありがとうございました。

```html
<!DOCTYPE html>
<html lang="ja">
<head>
<meta charset="utf-8">
<title>Memorial Video</title>
<link href="https://fonts.googleapis.com/css2?family=Noto+Sans+JP:wght@400;700;900&family=Noto+Serif+JP:wght@700;900&family=Roboto:wght@900&family=Parisienne&display=swap" rel="stylesheet">
<style>
:root{
  --green:#8cc63f;
  --green-deep:#5a9a1c;
  --green-pale:#e6f3cf;
  --green-mist:#f3f9e8;
  --ink:#333;
  --white:#fff;
}
*{margin:0;padding:0;box-sizing:border-box}
html,body{width:847px;height:1200px;overflow:hidden;background:var(--white)}
body{font-family:"Noto Sans JP",sans-serif;color:var(--ink);position:relative}
.abs{position:absolute}

.hero-photo{left:0;top:0;width:847px;height:430px;background:linear-gradient(135deg,#7e9a55 0%,#b8c98a 35%,#e9ede0 60%,#8aa066 100%)}
.hotel-name{right:26px;top:26px;color:var(--white);font-family:"Noto Serif JP",serif;font-size:12px;letter-spacing:1px}
.hero-title{left:22px;top:16px;font-family:"Roboto",sans-serif;font-weight:900;color:rgba(255,255,255,.9);font-size:100px;line-height:92px;letter-spacing:-2px;text-shadow:0 2px 6px rgba(0,0,0,.15)}
.catch{left:0;top:290px;width:400px;height:92px;background:linear-gradient(90deg,var(--green) 75%,rgba(140,198,63,0));padding:12px 0 0 70px;color:var(--white);font-family:"Noto Serif JP",serif;font-weight:900;font-size:24px;line-height:34px;border-radius:0 46px 46px 0}

.section-band{left:0;width:847px}
.band-memorial{top:420px;height:300px;background:linear-gradient(180deg,var(--green-pale),var(--white))}
.band-endrole{top:720px;height:265px;background:linear-gradient(180deg,var(--green-mist),var(--white))}
.script{font-family:"Parisienne",cursive;color:var(--green-deep);font-size:34px;line-height:32px;transform:rotate(-8deg)}
.heading{font-family:"Noto Serif JP",serif;font-weight:900;color:var(--white);background:var(--green);padding:6px 16px;border-radius:20px;font-size:22px}
.body-text{font-size:13px;line-height:22px}
.note{font-size:10px;color:#666}

.price-table{border-collapse:collapse;font-size:14px;font-weight:700}
.price-table th,.price-table td{border:1px solid var(--green);padding:8px 10px;text-align:center}
.price-table th{background:var(--green);color:var(--white)}
.price-table td{background:var(--white)}
.price-table td.label{background:var(--green-mist);text-align:left}

.option-row{display:flex;justify-content:space-between;background:var(--white);border:1px solid var(--green);padding:4px 12px;font-weight:700;font-size:14px;width:360px}
.option-desc{font-size:10px;color:#555;margin:3px 0 9px 6px}

.film-strip{left:0;top:990px;width:847px;height:95px;background:#222;display:flex;gap:8px;padding:12px 8px}
.film-frame{flex:1;background:linear-gradient(135deg,#a9c07a,#e8ecd6);border-radius:3px}
.footer{left:0;top:1092px;width:847px;height:58px;background:var(--green);display:flex;justify-content:space-between;align-items:center;padding:0 40px;color:var(--white);font-family:"Noto Serif JP",serif;font-weight:900;font-size:26px}
.disclaimer{left:40px;top:1158px;width:767px;font-size:10px;color:#666;line-height:16px;text-align:center}
</style>
</head>
<body>
  <div class="abs hero-photo" role="img" aria-label="新郎新婦が笑顔で寄り添う屋外の写真"></div>
  <div class="abs hotel-name">HOTEL VERDE GARDEN</div>
  <h1 class="abs hero-title">Memorial<br>Video</h1>
  <p class="abs catch">一生に一度の最高の舞台を<br>より感動的に残しませんか？</p>

  <section class="abs section-band band-memorial"></section>
  <div class="abs script" style="left:20px;top:436px">Memorial<br>&nbsp;&nbsp;Video</div>
  <h2 class="abs heading" style="left:170px;top:446px">挙式披露宴メモリアルビデオ</h2>
  <p class="abs body-text" style="left:30px;top:515px;width:400px">生涯一度の大切な瞬間…。だからこそ思い出の記録は、経験豊富なプロのカメラマンにお任せください。ご家族の祝辞、ご友人の演奏やスピーチ、クリアな映像と音声で、お届けします。</p>
  <table class="abs price-table" style="left:450px;top:500px">
    <tr><th></th><th>メニュー無し</th><th>メニュー有</th></tr>
    <tr><td class="label">挙式のみ</td><td>¥60,900</td><td>¥76,650</td></tr>
    <tr><td class="label">披露宴のみ</td><td>¥105,000</td><td>¥131,250</td></tr>
    <tr><td class="label">挙式・披露宴</td><td>¥136,500</td><td>¥162,750</td></tr>
  </table>
  <p class="abs note" style="left:600px;top:668px">※料金は全て税込となっております</p>

  <section class="abs section-band band-endrole"></section>
  <div class="abs script" style="left:16px;top:728px">Endrole<br>&nbsp;Movie</div>
  <h2 class="abs heading" style="left:150px;top:740px;line-height:28px;font-size:20px">撮って出し<br>エンドロールムービー</h2>
  <p class="abs body-text" style="left:30px;top:818px;width:370px">映画のようなクレジットの流れるエンディング…。ご二人のイメージ映像や舞台裏など、多数のカットで構成される披露宴の締めくくりを演出できます。</p>
  <div class="abs" style="left:30px;top:900px;width:370px">
    <div class="option-row" style="width:370px"><span>単品</span><span>¥136,500</span></div>
    <div class="option-row" style="width:370px;margin-top:6px"><span>プラス</span><span>¥36,500</span></div>
  </div>

  <div class="abs script" style="left:432px;top:738px">Option</div>
  <h2 class="abs heading" style="left:555px;top:738px">追加サービス</h2>
  <div class="abs" style="left:440px;top:792px">
    <div class="option-row"><span>ハイビジョン仕上げ</span><span>¥52,500</span></div>
    <p class="option-desc">高画質のHD映像をブルーレイディスクに収録します。</p>
    <div class="option-row"><span>外式会場撮影</span><span>¥10,500</span></div>
    <p class="option-desc">当ホテル以外の教会・神社での挙式を撮影します。</p>
    <div class="option-row"><span>ディスクコピー</span><span>¥10,500</span></div>
    <p class="option-desc">完成した映像の複製盤をお作りします。</p>
  </div>

  <div class="abs film-strip">
    <div class="film-frame" role="img" aria-label="挙式の一場面の写真"></div>
    <div class="film-frame" role="img" aria-label="披露宴の一場面の写真"></div>
    <div class="film-frame" role="img" aria-label="ウェディングケーキの写真"></div>
    <div class="film-frame" role="img" aria-label="ブーケの写真"></div>
    <div class="film-frame" role="img" aria-label="乾杯の場面の写真"></div>
    <div class="film-frame" role="img" aria-label="会場装花の写真"></div>
  </div>

  <footer class="abs footer">
    <span>Studio Hanamori Films</span>
    <span>TEL/FAX：029-555-0148</span>
  </footer>
  <p class="abs disclaimer">※撮影・編集内容は事前にお打ち合わせのうえ決定いたします。<br>詳しくは担当スタッフまでお気軽にお問い合わせください。</p>
</body>
</html>
```